Varemo Group Business Card Design

The CEO is looking for a new trendy look for his business card.
You can stay with current branding or come up with something new/creative. It can be 3D, including Medical Office buildings. You can use our logo in a variety of colors. Please include name, title, company name, company website, email address, cell number

Target Market(s)

Real Estate Development and Construction

Industry/Entity Type

Health care real estate

Contact Information for Business Card

Rohesh Kumbar, CEO M-727.418.9062 E-roheshkumbar@varemo.com Address:4100 Lindell Ave, Tampa, FL 33611 www.varemo.com

Font styles to use
Other font styles liked:
• Be creative

Requirements
Must have
• Creative, trendy look
Nice to have
• Please go to our website to get a feel- www. varemo.com
Should not have
• small fonts

```html
<!DOCTYPE html>
<html lang="en">
<head>
<meta charset="utf-8">
<title>Varemo Group Business Card</title>
<link rel="stylesheet" href="https://fonts.googleapis.com/css2?family=Lato:wght@400;900&family=Roboto:wght@400;700&display=swap">
<style>
  :root {
    --brand-red: #b01f29;
    --navy: #1d2b4f;
    --ink: #1a1a1a;
    --paper: #ffffff;
    --stage-inner: #3c3c3c;
    --stage-outer: #161616;
  }
  * { box-sizing: border-box; margin: 0; padding: 0; }
  html, body { width: 1200px; height: 1000px; overflow: hidden; }
  body {
    position: relative;
    background: radial-gradient(ellipse at 50% 45%, var(--stage-inner) 0%, #2a2a2a 50%, var(--stage-outer) 100%);
    font-family: "Lato", sans-serif;
  }
  .card {
    position: absolute;
    left: 214px;
    width: 772px;
    height: 440px;
    border-radius: 28px;
    overflow: hidden;
  }
  .card--front { top: 36px; background: var(--brand-red); }
  .card--back { top: 498px; background: var(--paper); }

  .company-name {
    position: absolute;
    font-family: "Lato", sans-serif;
    font-weight: 900;
    line-height: 1;
    white-space: nowrap;
  }
  .card--front .company-name {
    left: 0; width: 772px; top: 192px;
    text-align: center;
    font-size: 60px;
    color: var(--paper);
  }
  .card--back .company-name {
    left: 60px; width: 256px; top: 200px;
    text-align: right;
    font-size: 32px;
    color: var(--brand-red);
  }

  .divider {
    position: absolute;
    left: 352px; top: 102px;
    height: 222px;
    border-left: 2px dotted #444;
  }
  .contact { position: absolute; left: 402px; top: 98px; }
  .contact__name {
    font-family: "Roboto", sans-serif;
    font-weight: 700;
    font-size: 35px;
    color: var(--brand-red);
    letter-spacing: 0.5px;
    line-height: 1;
  }
  .contact__title {
    font-family: "Roboto", sans-serif;
    font-weight: 700;
    font-size: 20px;
    color: var(--navy);
    margin-top: 2px;
    margin-left: 1px;
  }
  .contact__address {
    font-size: 20.5px;
    color: var(--ink);
    line-height: 25px;
    margin-top: 10px;
  }
  .contact__list { list-style: none; margin-top: 13px; }
  .contact__item {
    display: flex; align-items: center;
    font-family: "Roboto", sans-serif;
    font-size: 20px;
    color: var(--ink);
    height: 31px;
  }
  .contact__icon { width: 20px; height: 22px; margin-right: 10px; flex: none; }
  .card__swoosh { position: absolute; left: 0; bottom: 0; width: 772px; height: 70px; display: block; }
</style>
</head>
<body>

<section class="card card--front">
  <p class="company-name">Varemo Group</p>
</section>

<section class="card card--back">
  <p class="company-name">Varemo Group</p>

  <div class="divider"></div>

  <div class="contact">
    <h1 class="contact__name">ROHESH KUMBAR</h1>
    <p class="contact__title">CEO</p>
    <p class="contact__address">4100 Lindell Ave,Tampa,<br>FL 33611</p>
    <ul class="contact__list">
      <li class="contact__item">
        <svg class="contact__icon" viewBox="0 0 20 22" aria-hidden="true">
          <rect x="4" y="1" width="12" height="20" rx="2" fill="none" stroke="var(--navy)" stroke-width="1.8"/>
          <line x1="8" y1="17.5" x2="12" y2="17.5" stroke="var(--navy)" stroke-width="1.6"/>
        </svg>
        M-727.418.9062
      </li>
      <li class="contact__item">
        <svg class="contact__icon" viewBox="0 0 20 22" aria-hidden="true">
          <path d="M1 11 L19 3 L14 20 L10 13 Z" fill="var(--navy)"/>
          <path d="M10 13 L19 3" stroke="#fff" stroke-width="1.2"/>
        </svg>
        roheshkumbar@varemo.com
      </li>
      <li class="contact__item">
        <svg class="contact__icon" viewBox="0 0 20 22" aria-hidden="true">
          <g fill="none" stroke="var(--navy)" stroke-width="1.5">
            <circle cx="10" cy="11" r="8"/>
            <ellipse cx="10" cy="11" rx="3.5" ry="8"/>
            <line x1="2" y1="11" x2="18" y2="11"/>
            <path d="M3.5 6.5 H16.5 M3.5 15.5 H16.5"/>
          </g>
        </svg>
        www.varemo.com
      </li>
    </ul>
  </div>

  <svg class="card__swoosh" viewBox="0 0 772 70" aria-hidden="true">
    <rect x="0" y="0" width="772" height="70" fill="var(--brand-red)"/>
    <path d="M0 0 H772 V16 Q420 58 0 7 Z" fill="var(--paper)"/>
    <path d="M51 9 Q400 44 726 19 Q400 33 51 9 Z" fill="var(--navy)"/>
  </svg>
</section>

</body>
</html>
```